Psychotherapy, Life Coaching, Writer, Motivational Speaker

I am a psychotherapist, life coach, writer and speaker on health and wellness issues. I am a humanist - who believes that we are born to self-actualize - but life - changes that course. That we develop armor and coping mechanisms that divert our growth. I help people examine their road blocks to happiness. My business is unique in that I do concierge therapy. I work intensively - with multi-day sessions, I work internationally through tele-therapy - and traditionally - in an office space. My work is tailored to your needs.

Target Market(s)

Broad

Industry/Entity Type

Health

Contact Information for Business Card

Listen To Grow
Sam Virelle
482 East 23rd Street
New York, NY 10027
(305) 418-7302

Requirements
Must have
• Clean lines... not too busy...
• FB page listing: Listen To Grow
• my Web page: www.listentogrow-example.com
Nice to have
• I would love to be able to list the services: Psychotherapist, Life Coach, Motivational Speaker and Writer - but also don't want a crazy crowded card. Feel free to use the back for description.
Should not have
• Stay away from corny imagery - lotus flowers, zen, lily pond, clouds.

```html
<!DOCTYPE html>
<html lang="en">
<head>
<meta charset="utf-8">
<title>Listen To Grow – Business Card</title>
<link rel="stylesheet" href="https://fonts.googleapis.com/css2?family=Open+Sans:wght@400;600;700&display=swap">
<style>
  :root {
    --brand-blue: #0a70bd;
    --card-white: #f3f3f1;
    --backdrop: #d9d9d9;
    --ink-light: #ffffff;
  }
  * { margin: 0; padding: 0; box-sizing: border-box; }
  html, body {
    width: 1200px;
    height: 1018px;
    overflow: hidden;
    background: var(--backdrop);
    font-family: "Open Sans", Arial, sans-serif;
  }
  .sheet {
    position: relative;
    width: 1200px;
    height: 1018px;
  }
  .card {
    position: absolute;
    left: 180px;
    width: 840px;
    height: 480px;
    overflow: hidden;
    box-shadow: 0 4px 14px rgba(0,0,0,0.15);
  }
  .card--front { top: 20px; background: var(--card-white); }
  .card--back  { top: 518px; background: var(--brand-blue); }

  .contact-panel {
    position: absolute;
    left: 420px;
    top: 0;
    width: 420px;
    height: 270px;
    background: var(--brand-blue);
    color: var(--ink-light);
    padding: 22px 24px;
    font-size: 21px;
    line-height: 1.32;
    letter-spacing: 0.3px;
  }
  .contact-name { font-weight: 700; font-size: 24px; margin-bottom: 2px; }
  .contact-phone { font-size: 23px; }
  .contact-row { display: flex; align-items: center; gap: 8px; font-size: 19px; letter-spacing: 0.8px; }
  .social-mark {
    width: 15px; height: 15px;
    background: var(--ink-light);
    flex: none;
  }
  .home-icon { width: 17px; height: 15px; flex: none; }

  .accent-rule {
    position: absolute;
    left: 0;
    top: 222px;
    width: 420px;
    height: 10px;
    background: var(--brand-blue);
  }
  .accent-divider {
    position: absolute;
    left: 418px;
    top: 270px;
    width: 3px;
    height: 150px;
    background: var(--brand-blue);
  }
  .brand-name {
    position: absolute;
    right: 432px;
    top: 240px;
    color: var(--brand-blue);
    font-weight: 700;
    font-size: 34px;
    letter-spacing: 0.5px;
    text-transform: uppercase;
    white-space: nowrap;
  }

  .services {
    position: absolute;
    inset: 0;
    display: flex;
    flex-direction: column;
    align-items: center;
    justify-content: center;
    color: var(--ink-light);
    font-size: 22px;
    letter-spacing: 2px;
    line-height: 1.3;
    text-align: center;
    padding-bottom: 40px;
  }
</style>
</head>
<body>
<main class="sheet">
  <section class="card card--front" aria-label="Business card front">
    <div class="contact-panel">
      <p class="contact-name">Sam Virelle</p>
      <p>482 East 23rd Street</p>
      <p>New York, NY 10027</p>
      <p class="contact-phone">(305) 418-7302</p>
      <p class="contact-row"><span class="social-mark"></span>ListenToGrow</p>
      <p class="contact-row">
        <svg class="home-icon" viewBox="0 0 17 15" aria-hidden="true">
          <path d="M8.5 0 L17 7.5 H14.5 V15 H10.5 V10 H6.5 V15 H2.5 V7.5 H0 Z" fill="#ffffff"/>
        </svg>
        www.listentogrow-example.com
      </p>
    </div>
    <div class="accent-rule"></div>
    <p class="brand-name">Listen To Grow</p>
    <div class="accent-divider"></div>
  </section>

  <section class="card card--back" aria-label="Business card back">
    <div class="services">
      <p>Psychotherapist</p>
      <p>Life Coach</p>
      <p>Motivational Speaker and Writer</p>
    </div>
  </section>
</main>
</body>
</html>
```